Clearstep Foot Care patient advertisement flyer

We need a flyer for a new fungal nail treatment clinic called clearstep foot care. We require a flyer/brochure that advertises our clinic and what we do (please find attached a document that has the information we would like included - we are completely open to the designer structuring the information how they see fit so long as it encompasses the information provided). We also have a booklet that we give to patients on their initial consult (which I have attached to give you an idea of the colour schemes /design that we are already using and we would like our brochure to align with this booklet). I have also attached our logo for use in the brochure. Finally, I have attached a copy of our cold laser brochure and associated pictures - ideally we would like to capture something similar to this brochure and have a picture of the laser somewhere on the brochure. We would like our brochure to communicate professional but be sleek, modern and have a minimalist look.
Updates

Can we please make these tri fold outs please like a brochure format 😊

```html
<!DOCTYPE html>
<html lang="en">
<head>
<meta charset="utf-8">
<title>Clearstep Foot Care – Tri-fold Brochure</title>
<link href="https://fonts.googleapis.com/css2?family=Libre+Baskerville:wght@400;700&family=Open+Sans:wght@400;600;700&display=swap" rel="stylesheet">
<style>
  :root {
    --page-bg: #e8eaed;
    --paper: #ffffff;
    --brand-blue: #3d6cc0;
    --brand-blue-dark: #234a8f;
    --brand-navy: #1f3563;
    --tint-blue: #dde6f5;
    --text-body: #4a5468;
    --photo-blue-a: #2c4f96;
    --photo-blue-b: #6f92d4;
  }
  * { box-sizing: border-box; margin: 0; padding: 0; }
  html, body { width: 1200px; height: 2400px; overflow: hidden; }
  body {
    background: var(--page-bg);
    font-family: "Open Sans", sans-serif;
    color: var(--text-body);
    position: relative;
  }
  .spread {
    position: absolute;
    left: 50px;
    width: 1100px;
    height: 850px;
    display: flex;
    background: var(--paper);
    box-shadow: 0 12px 30px rgba(30, 45, 80, 0.15);
    overflow: hidden;
  }
  .spread--outside { top: 250px; }
  .spread--inside { top: 1300px; }
  .panel {
    position: relative;
    width: 366.67px;
    height: 100%;
    padding: 48px 40px;
  }
  .panel + .panel { border-left: 1px solid rgba(0, 0, 0, 0.05); }
  .photo {
    border-radius: 50%;
    background: radial-gradient(circle at 35% 35%, var(--photo-blue-b), var(--photo-blue-a));
  }
  .photo--ring { box-shadow: 0 0 0 8px var(--tint-blue); }
  .body-copy { font-size: 14px; line-height: 1.7; margin-bottom: 16px; }
  .section-title {
    font-family: "Libre Baskerville", serif;
    font-size: 18px;
    color: var(--brand-navy);
    margin-bottom: 10px;
    line-height: 1.35;
  }

  /* Brand name lockup */
  .brand { display: flex; align-items: center; gap: 14px; }
  .brand-dot { width: 44px; height: 44px; border-radius: 50%; background: var(--brand-blue); flex: none; }
  .brand-name {
    font-family: "Libre Baskerville", serif;
    font-weight: 700;
    font-size: 22px;
    line-height: 1.2;
    letter-spacing: 0.06em;
    color: var(--brand-navy);
    text-transform: uppercase;
  }

  /* Outside: info flap */
  .flap .photo { width: 220px; height: 220px; margin: 0 auto 36px; background: radial-gradient(circle at 40% 40%, #e7a6c4, #b84f86); }

  /* Outside: back panel */
  .back { background: var(--brand-blue); color: #fff; text-align: center; padding: 0; }
  .back-photo {
    height: 330px;
    background: linear-gradient(180deg, rgba(255,255,255,0.12), rgba(61,108,192,1)), linear-gradient(135deg, var(--photo-blue-a), var(--photo-blue-b));
  }
  .back-body { padding: 0 40px; margin-top: -40px; position: relative; }
  .back .brand { justify-content: center; margin-bottom: 40px; }
  .back .brand-dot { background: #fff; }
  .back .brand-name { color: #fff; font-size: 18px; }
  .social-row { display: flex; justify-content: center; gap: 16px; margin-bottom: 40px; }
  .social-dot { width: 38px; height: 38px; border-radius: 50%; border: 2px solid rgba(255,255,255,0.85); }
  .contact-list { list-style: none; font-size: 14px; line-height: 2.1; }
  .contact-list li { display: flex; align-items: center; justify-content: center; gap: 10px; }

  /* Outside: cover */
  .cover { text-align: left; }
  .cover .brand { margin-bottom: 44px; }
  .cover .photo { width: 280px; height: 280px; margin: 0 auto 44px; }
  .cover-title {
    font-family: "Libre Baskerville", serif;
    font-size: 27px;
    line-height: 1.35;
    color: var(--brand-navy);
    text-transform: uppercase;
    letter-spacing: 0.02em;
    margin-bottom: 36px;
  }
  .pill {
    display: block;
    background: var(--brand-blue);
    color: #fff;
    border-radius: 30px;
    padding: 14px 20px;
    text-align: center;
    font-weight: 600;
    font-size: 15px;
  }

  /* Inside */
  .inside-band {
    position: absolute; left: 0; right: 0; bottom: 0; height: 150px;
    background: var(--tint-blue);
  }
  .inside-left .photo { width: 230px; height: 230px; margin: 0 0 34px; background: radial-gradient(circle at 40% 40%, #f2ddd2, #b8c9e6); }
  .inside-middle .photo { width: 250px; height: 250px; margin: 28px auto 0; position: relative; z-index: 1; }
  .thumb-grid { display: grid; grid-template-columns: 110px 110px; gap: 18px; justify-content: center; margin-bottom: 30px; }
  .thumb { width: 110px; height: 110px; border-radius: 50%; }
  .thumb--a { background: radial-gradient(circle, #d9b69a, #9c7157); }
  .thumb--b { background: radial-gradient(circle, #d7c5a8, #8f7a55); }
  .thumb--c { background: radial-gradient(circle, #b9a77e, #6d5f3f); }
  .thumb--d { background: radial-gradient(circle, #e2c3ad, #a88068); }
  .cta-bar {
    background: var(--brand-blue); color: #fff; text-align: center;
    font-weight: 600; font-size: 15px; padding: 12px; margin: 10px 0 40px;
  }
  .inside-right .brand { justify-content: center; position: relative; z-index: 1; }
  .inside-right .brand-name { font-size: 18px; }
  .panel > * { position: relative; }
</style>
</head>
<body>

<!-- Outside spread: flap, back, cover -->
<section class="spread spread--outside">
  <article class="panel flap">
    <div class="photo photo--ring" role="img" aria-label="Close-up of painted toenails"></div>
    <h3 class="section-title">Healthy nails start here</h3>
    <p class="body-copy">Fungal nail infections are common and often stubborn. Early care helps restore healthy, clear nails.</p>
    <p class="body-copy">Our clinic offers gentle cold laser treatment with no downtime, tailored to each patient.</p>
    <p class="body-copy">Book a consult to review your nails and plan a treatment path that suits you.</p>
  </article>

  <article class="panel back">
    <div class="back-photo" role="img" aria-label="Blue-toned photo of bare feet"></div>
    <div class="back-body">
      <div class="brand">
        <span class="brand-dot"></span>
        <span class="brand-name">Clearstep<br>Foot Care</span>
      </div>
      <div class="social-row">
        <span class="social-dot"></span><span class="social-dot"></span><span class="social-dot"></span><span class="social-dot"></span>
      </div>
      <ul class="contact-list">
        <li>
          <svg width="14" height="14" viewBox="0 0 24 24" fill="#fff"><path d="M6.6 10.8a15 15 0 0 0 6.6 6.6l2.2-2.2c.3-.3.7-.4 1-.2 1.1.4 2.3.6 3.6.6.6 0 1 .4 1 1V20c0 .6-.4 1-1 1A17 17 0 0 1 3 4c0-.6.4-1 1-1h3.5c.6 0 1 .4 1 1 0 1.3.2 2.5.6 3.6.1.3 0 .7-.2 1z"/></svg>
          (02) 5550 1842
        </li>
        <li>hello@clearstepfootcare.com</li>
        <li>www.clearstepfootcare.com</li>
        <li>
          <svg width="12" height="14" viewBox="0 0 24 28" fill="#fff"><path d="M12 0a10 10 0 0 0-10 10c0 7.5 10 18 10 18s10-10.5 10-18A10 10 0 0 0 12 0zm0 14a4 4 0 1 1 0-8 4 4 0 0 1 0 8z"/></svg>
          12 Harbour Lane, Westfield
        </li>
      </ul>
    </div>
  </article>

  <article class="panel cover">
    <div class="brand">
      <span class="brand-dot"></span>
      <span class="brand-name">Clearstep<br>Foot Care</span>
    </div>
    <div class="photo photo--ring" role="img" aria-label="Blue-toned photo of feet in a treatment setting"></div>
    <h1 class="cover-title">Your complete guide to fungal nail infections</h1>
    <span class="pill">Book your consultation today</span>
  </article>
</section>

<!-- Inside spread -->
<section class="spread spread--inside">
  <div class="inside-band"></div>

  <article class="panel inside-left">
    <div class="photo photo--ring" role="img" aria-label="Hand holding a foot to examine a toenail"></div>
    <h3 class="section-title">What is a fungal nail infection?</h3>
    <p class="body-copy">A fungal infection develops under or around the nail, causing thickening, yellowing and brittle edges over time.</p>
    <h3 class="section-title">Common signs</h3>
    <p class="body-copy">Discoloured, thick or crumbling nails, a mild odour and separation from the nail bed.</p>
  </article>

  <article class="panel inside-middle">
    <h3 class="section-title">How cold laser works</h3>
    <p class="body-copy">Low level laser light passes through the nail to target fungus without heat or pain. Sessions are quick and safe.</p>
    <div class="photo photo--ring" role="img" aria-label="Clinician applying cold laser treatment to a foot"></div>
  </article>

  <article class="panel inside-right">
    <div class="thumb-grid">
      <div class="thumb thumb--a" role="img" aria-label="Toenail with mild infection"></div>
      <div class="thumb thumb--b" role="img" aria-label="Toenail with yellow discolouration"></div>
      <div class="thumb thumb--c" role="img" aria-label="Thickened infected toenail"></div>
      <div class="thumb thumb--d" role="img" aria-label="Toenail after treatment"></div>
    </div>
    <p class="body-copy">Each session takes around twenty minutes and most patients need a short course.</p>
    <div class="cta-bar">Call to book today</div>
    <div class="brand">
      <span class="brand-dot"></span>
      <span class="brand-name">Clearstep<br>Foot Care</span>
    </div>
  </article>
</section>

</body>
</html>
```